Business Cards

I'd like help creating business cards with the full logo "Veltrona Capital Partners" on the back of the card (navy background with white writing), and abbreviated logo "VCP" on the front. Would like to list name, title, phone number, email, and website listed on front of card. Would like to keep very simple. Front font Arial or similar.

```html
<!DOCTYPE html>
<html lang="en">
<head>
<meta charset="utf-8">
<title>Veltrona Capital Partners – Business Cards</title>
<link href="https://fonts.googleapis.com/css2?family=Arimo:wght@400;700&display=swap" rel="stylesheet">
<style>
  :root {
    --navy: #1d3969;
    --white: #ffffff;
    --backdrop: #3a3a3a;
    --rule: rgba(255,255,255,0.55);
  }
  * { margin: 0; padding: 0; box-sizing: border-box; }
  html, body { width: 1200px; height: 689px; overflow: hidden; }
  body {
    background: var(--backdrop);
    font-family: "Arimo", Arial, sans-serif;
    position: relative;
  }
  .card {
    position: absolute;
    top: 196px;
    width: 520px;
    height: 297px;
    border-radius: 18px;
    overflow: hidden;
  }
  .card-back {
    left: 50px;
    background: var(--navy);
    display: flex;
    align-items: center;
    justify-content: center;
  }
  .brand-full {
    color: var(--white);
    font-weight: 700;
    text-align: center;
    display: flex;
    align-items: center;
    gap: 14px;
  }
  .brand-square {
    width: 22px;
    height: 22px;
    background: var(--white);
    flex: none;
  }
  .brand-name {
    font-size: 40px;
    letter-spacing: 1px;
    line-height: 1;
    text-transform: uppercase;
  }
  .brand-sub {
    display: block;
    font-size: 17px;
    letter-spacing: 6px;
    margin-top: 10px;
  }
  .card-front {
    left: 630px;
    background: var(--white);
  }
  .front-logo {
    position: absolute;
    left: 0; right: 0; top: 0;
    height: 178px;
    display: flex;
    align-items: center;
    justify-content: center;
    gap: 14px;
    color: var(--navy);
  }
  .front-logo .brand-square { background: var(--navy); width: 26px; height: 26px; }
  .front-logo .brand-name { font-size: 76px; letter-spacing: 4px; font-weight: 700; }
  .front-band {
    position: absolute;
    left: 0; right: 0; bottom: 0;
    height: 119px;
    background: var(--navy);
    color: var(--white);
    display: flex;
    align-items: center;
    justify-content: center;
    gap: 22px;
  }
  .holder { text-align: right; }
  .holder-name { font-size: 20px; font-weight: 700; letter-spacing: 0.5px; }
  .holder-title { font-size: 12px; margin: 2px 0 6px; }
  .holder-address { font-size: 11.5px; line-height: 1.4; }
  .divider { width: 1px; height: 82px; background: var(--rule); }
  .contacts { list-style: none; font-size: 12px; line-height: 1.6; }
  .contacts li { display: flex; align-items: center; gap: 8px; }
  .contacts svg { width: 11px; height: 11px; flex: none; }
</style>
</head>
<body>

<section class="card card-back" aria-label="Card back">
  <div class="brand-full">
    <span class="brand-square"></span>
    <div>
      <span class="brand-name">Veltrona</span>
      <span class="brand-sub">CAPITAL PARTNERS</span>
    </div>
  </div>
</section>

<section class="card card-front" aria-label="Card front">
  <div class="front-logo">
    <span class="brand-square"></span>
    <span class="brand-name">VCP</span>
  </div>
  <div class="front-band">
    <div class="holder">
      <p class="holder-name">DANIEL HARTLEY</p>
      <p class="holder-title">President</p>
      <p class="holder-address">4120 Maple Ridge Road<br>Halford, Canada 20813</p>
    </div>
    <span class="divider"></span>
    <ul class="contacts">
      <li>
        <svg viewBox="0 0 12 12"><path d="M2.5 1h2l1 3-1.3 1a6.5 6.5 0 0 0 2.8 2.8L8 6.5l3 1v2a1.5 1.5 0 0 1-1.5 1.5A8.5 8.5 0 0 1 1 2.5 1.5 1.5 0 0 1 2.5 1z" fill="#fff"/></svg>
        555-218-4702
      </li>
      <li>
        <svg viewBox="0 0 12 12"><rect x="3" y="0.5" width="6" height="11" rx="1" fill="none" stroke="#fff"/><circle cx="6" cy="9.5" r="0.7" fill="#fff"/></svg>
        555-391-6087
      </li>
      <li>
        <svg viewBox="0 0 12 12"><rect x="0.5" y="2" width="11" height="8" fill="none" stroke="#fff"/><path d="M0.5 2 6 6.5 11.5 2" fill="none" stroke="#fff"/></svg>
        info@VCP.com
      </li>
      <li>
        <svg viewBox="0 0 12 12"><circle cx="6" cy="6" r="5.3" fill="none" stroke="#fff"/><ellipse cx="6" cy="6" rx="2.3" ry="5.3" fill="none" stroke="#fff"/><path d="M0.7 6h10.6" stroke="#fff"/></svg>
        www.VCP.com
      </li>
    </ul>
  </div>
</section>

</body>
</html>
```